Mobile technology Business Card Design Project

We need a business card design for our company based in Sydeny Australia, that takes a company's desktop sites and creates a mobile site compatible to all mobile/smartphone devices. This allows greater ease of use and generally faster business conversion than customers using a desktop site.
Our company is called VelqCore but we refer to it as Velq Corestreams. If this could be represented somewhere on the business card that would be great.
Am open to suggestions regarding the colours but a high tech  theme would be good.
Happy bidding!

Target Market(s)
Business owner that has a website and is reasonably savvy regarding online/mobile marketing.
Industry/Entity Type
Business
Requirements
Must have
- Business card details:
Director Peter Langwade
Address: 5/41 Dunmore rd, Kelbrook. 2087
Email: tbc
Web: www.velqcore.com.au
The cards need to have two different names for the two directors.
Gregory Halvane & Peter Langwade (two separate business cards)

```html
<!DOCTYPE html>
<html lang="en">
<head>
<meta charset="utf-8">
<title>VelqCore Business Card</title>
<link href="https://fonts.googleapis.com/css2?family=Questrial&family=Crimson+Text:wght@400;600&display=swap" rel="stylesheet">
<style>
  :root {
    --backdrop: #4a2b1d;
    --front-light: #f8f8f8;
    --front-edge: #cdcccc;
    --back-light: #4ba6da;
    --back-edge: #2f86b8;
    --brand-blue: #1f9bd7;
    --brand-orange: #f0901e;
    --ink-dark: #222222;
    --paper-white: #ffffff;
  }
  html, body {
    margin: 0;
    width: 1200px;
    height: 1181px;
    overflow: hidden;
    background: var(--backdrop);
  }
  .canvas {
    position: relative;
    width: 1200px;
    height: 1181px;
  }
  .card {
    position: absolute;
    left: 206px;
    width: 786px;
    height: 452px;
    border-radius: 30px;
    overflow: hidden;
  }
  .card-front {
    top: 100px;
    background: radial-gradient(ellipse at 50% 45%, var(--front-light) 0%, var(--front-light) 20%, var(--front-edge) 100%);
  }
  .card-back {
    top: 619px;
    background: radial-gradient(ellipse at 50% 45%, var(--back-light) 0%, var(--back-edge) 100%);
    color: var(--paper-white);
    font-family: "Crimson Text", serif;
    text-align: center;
  }
  .front-dot {
    position: absolute;
    left: 313px;
    top: 107px;
    width: 176px;
    height: 176px;
    border-radius: 50%;
    background: var(--brand-blue);
  }
  .brand-name {
    position: absolute;
    left: 0;
    width: 100%;
    top: 284px;
    margin: 0;
    line-height: 44px;
    text-align: center;
    font-family: "Questrial", sans-serif;
    font-size: 38px;
    font-weight: 400;
    color: var(--ink-dark);
  }
  .brand-tagline {
    position: absolute;
    left: 0;
    width: 100%;
    top: 326px;
    margin: 0;
    line-height: 20px;
    text-align: center;
    font-family: "Questrial", sans-serif;
    font-size: 16px;
    letter-spacing: 0.5px;
    color: var(--brand-orange);
  }
  .back-tagline {
    position: absolute;
    top: 16px;
    left: 0;
    width: 100%;
    margin: 0;
    line-height: 22px;
    font-size: 17px;
  }
  .back-brand {
    position: absolute;
    top: 204px;
    left: 0;
    width: 100%;
    height: 48px;
    margin: 0;
    display: flex;
    align-items: center;
    justify-content: center;
    gap: 12px;
    font-size: 36px;
    line-height: 48px;
    font-weight: 400;
  }
  .back-dot {
    width: 36px;
    height: 36px;
    border-radius: 50%;
    background: var(--paper-white);
  }
  .person-name {
    position: absolute;
    top: 320px;
    left: 0;
    width: 100%;
    margin: 0;
    line-height: 32px;
    font-size: 27px;
    font-weight: 400;
    text-transform: uppercase;
    letter-spacing: 0.3px;
  }
  .person-role {
    position: absolute;
    top: 352px;
    left: 0;
    width: 100%;
    margin: 0;
    line-height: 26px;
    font-size: 21px;
  }
  .contact {
    position: absolute;
    top: 401px;
    left: 0;
    width: 100%;
    margin: 0;
    font-size: 15px;
    line-height: 21px;
    font-style: normal;
  }
  .contact .divider {
    margin: 0 12px;
  }
</style>
</head>
<body>
<div class="canvas">
  <section class="card card-front">
    <span class="front-dot" aria-hidden="true"></span>
    <h1 class="brand-name">VelqCore</h1>
    <p class="brand-tagline">Making Sites Mobile Ready</p>
  </section>

  <section class="card card-back">
    <p class="back-tagline">Faster business conversion with Velq Corestreams</p>
    <p class="back-brand"><span class="back-dot" aria-hidden="true"></span>VelqCore</p>
    <h2 class="person-name">Peter Langwade</h2>
    <p class="person-role">Director</p>
    <address class="contact">
      5/41 Dunmore rd, Kelbrook. 2087<br>
      name@velqcore.com<span class="divider">|</span>www.velqcore.com.au
    </address>
  </section>
</div>
</body>
</html>
```